Bref créative
Trucking Company Business Cards Stationary
KVR Freight Solutions
Professional
Beto Quiroga
Terminal Manager
4100 Harborview Blvd
La Porte, TX 77571
kvrfreightsolutions@mailbox-example.com
i would like something similar to this on the back side of card
i would also like something similar to this on the back side of my card

```html
<!DOCTYPE html>
<html lang="en">
<head>
<meta charset="utf-8">
<title>KVR Freight Solutions — Stationery</title>
<link href="https://fonts.googleapis.com/css2?family=Open+Sans:wght@400;600;800&display=swap" rel="stylesheet">
<style>
  :root{
    --bg:#e9eaec;
    --paper:#ffffff;
    --red:#b5151c;
    --red-dark:#8c0f14;
    --grey:#9a9ca0;
    --ink:#3a3b3d;
    --muted:#6d6f73;
  }
  *{box-sizing:border-box;margin:0;padding:0}
  html,body{width:1200px;height:936px;overflow:hidden}
  body{background:var(--bg);font-family:"Open Sans",Arial,sans-serif;color:var(--ink);position:relative}
  .piece{position:absolute;background:var(--paper);overflow:hidden}
  .piece svg.edge{position:absolute;inset:0;width:100%;height:100%}
  .brand{font-weight:800;color:var(--red);line-height:1;letter-spacing:.5px}
  .brand--white{color:#fff}

  /* letterhead */
  .letterhead{left:172px;top:63px;width:398px;height:557px}
  .letterhead .brand{position:absolute;left:50px;top:26px;font-size:13px}
  .letterhead .contact{position:absolute;left:250px;top:22px;font-size:5.4px;line-height:8px;color:var(--muted)}
  .letter{position:absolute;left:50px;top:100px;width:310px;font-size:5.6px;line-height:8.4px;color:var(--muted)}
  .letter p{margin-bottom:10px}
  .letter .signature{font-size:12px;color:var(--ink);font-style:normal;margin:4px 0 2px}
  .letter .sender{font-weight:600;color:var(--ink)}

  /* cover sheet */
  .cover{left:633px;top:38px;width:488px;height:595px}
  .cover .brand{position:absolute;left:0;right:40px;top:235px;text-align:center;font-size:46px}

  /* business cards */
  .card{width:154px;height:104px;left:94px}
  .card--front{top:653px}
  .card--back{top:777px}
  .card--front .panel{position:absolute;right:0;top:0;width:64px;height:100%;background:var(--red);display:flex;align-items:center;justify-content:center;text-align:center}
  .card--front .panel .brand{font-size:9px;padding:0 4px}
  .card--front .details{position:absolute;left:9px;top:12px;font-size:5px;line-height:7.5px;color:var(--muted);width:80px}
  .card--front .details strong{display:block;font-size:6.5px;color:var(--ink)}
  .card--back .brand{position:absolute;left:0;right:0;top:34px;text-align:center;font-size:11px}
  .card--back .strip{position:absolute;left:0;right:0;bottom:0;height:18px;background:var(--red);color:#fff;font-size:5.5px;text-align:center;line-height:18px;letter-spacing:.5px}

  /* envelopes */
  .envelope{top:670px;height:203px}
  .envelope--front{left:266px;width:430px}
  .envelope--front .brand{position:absolute;left:24px;top:28px;font-size:12px}
  .envelope--front .return{position:absolute;left:24px;top:50px;font-size:5.4px;line-height:8px;color:var(--muted)}
  .envelope--back{left:734px;width:387px}
  .envelope--back .url{position:absolute;left:0;right:0;top:34px;text-align:center;color:#fff;font-size:10px;letter-spacing:1px}
</style>
</head>
<body>

<section class="piece letterhead" aria-label="Letterhead">
  <svg class="edge" viewBox="0 0 398 557" preserveAspectRatio="none" aria-hidden="true">
    <path d="M0 0H24Q44 278 24 557H0Z" fill="var(--red)"/>
    <path d="M31 0Q53 278 31 557" fill="none" stroke="var(--grey)" stroke-width="2"/>
  </svg>
  <div class="brand">KVR Freight Solutions</div>
  <address class="contact" style="font-style:normal">
    4100 Harborview Blvd<br>
    La Porte, TX 77571<br>
    (281) 555-0148<br>
    (281) 555-0193<br>
    kvrfreightsolutions@mailbox-example.com
  </address>
  <div class="letter">
    <p>June 8, 2024</p>
    <p>Dear Sir,<br>ABC Building, 48 Main St, Anytown</p>
    <p>We are pleased to confirm our freight service agreement for the coming season. Our team will handle pickup, transport and delivery with care, on schedule and at the agreed rates.</p>
    <p>Please review the attached terms and contact us with any questions before the first shipment date.</p>
    <p>We look forward to a long and productive partnership with your company and your customers.</p>
    <p>Best Regards,</p>
    <div class="signature">~ B. Q.</div>
    <div class="sender">Beto Quiroga</div>
    <div>Terminal Manager</div>
  </div>
</section>

<section class="piece cover" aria-label="Cover sheet">
  <svg class="edge" viewBox="0 0 488 595" preserveAspectRatio="none" aria-hidden="true">
    <path d="M488 0H456Q426 298 456 595H488Z" fill="var(--red)"/>
    <path d="M447 0Q417 298 447 595" fill="none" stroke="var(--grey)" stroke-width="2"/>
  </svg>
  <div class="brand">KVR Freight Solutions</div>
</section>

<section class="piece card card--front" aria-label="Business card front">
  <div class="details">
    <strong>Beto Quiroga</strong>
    Terminal Manager<br>
    (281) 555-0148<br>
    4100 Harborview Blvd<br>
    La Porte, TX 77571
  </div>
  <div class="panel"><span class="brand brand--white">KVR Freight Solutions</span></div>
</section>

<section class="piece card card--back" aria-label="Business card back">
  <div class="brand">KVR Freight Solutions</div>
  <div class="strip">www.kvrfreight-example.com</div>
</section>

<section class="piece envelope envelope--front" aria-label="Envelope front">
  <div class="brand">KVR Freight Solutions</div>
  <address class="return" style="font-style:normal">
    4100 Harborview Blvd<br>
    La Porte, TX 77571
  </address>
</section>

<section class="piece envelope envelope--back" aria-label="Envelope back">
  <svg class="edge" viewBox="0 0 387 203" preserveAspectRatio="none" aria-hidden="true">
    <path d="M0 0H387V72Q193 112 0 72Z" fill="var(--red)"/>
    <path d="M0 80Q193 120 387 80" fill="none" stroke="var(--grey)" stroke-width="2"/>
  </svg>
  <div class="url">www.kvrfreight-example.com</div>
</section>

</body>
</html>
```